4th Generation Family Business Needs a New Card Design!

We are a family owned 4th Generation company. We are based in the Sydney, Australia area and we are desperately in need of a more modern and classy card. We are monumental masons who design, supply & erect lasting memorials throughout cemeteries in Sydney. Our customers are normally in a period of grieving. I have attached logo files that will need to be implemented on the card. Company was established 1935. Australian Owned and Operated. Card needs to be designed to PRINTLY.com specification.

Target Market(s)

Our target market is based upon people that a grieving for family members that have passed away. We also deal with alot of companies that own and operate cemeteries.

Industry/Entity Type

Business

Contact Information for Business Card

Gavin Pelham, Operations Manager, 0491726053, gavin@pelhamstoneworks.com.au
Brian Pelham, Director, 0417639285, brian@pelhamstoneworks.com.au
Phone # 02 9563 4820
Website: www.pelhamstoneworks.com.au
Address: Suite 17, 9 Lambert Lane, Kellyville, Sydney NSW 2155

Font styles to use
Serif
Decorative
Script

Requirements
Must have
• Would like to see the logo nicely implemented with a modern design. Embossed lettering would be a nice additive.

```html
<!DOCTYPE html>
<html lang="en">
<head>
<meta charset="utf-8">
<title>Pelham Stoneworks – Business Card</title>
<link href="https://fonts.googleapis.com/css2?family=Cinzel:wght@400;600;700&family=Open+Sans:wght@400;600&display=swap" rel="stylesheet">
<style>
  :root {
    --stage: #3a3330;
    --card-white: #ffffff;
    --card-dark: #1f2226;
    --ink: #1b1b1b;
    --gold: #f0c02f;
    --text-grey: #3c3c3c;
    --rule-grey: #cfcfcf;
    --silver: #b9bcc0;
  }
  * { box-sizing: border-box; margin: 0; padding: 0; }
  html, body { width: 1200px; height: 769px; overflow: hidden; }
  body {
    background: var(--stage);
    position: relative;
    font-family: "Open Sans", Arial, sans-serif;
  }
  .card {
    position: absolute;
    top: 236px;
    width: 520px;
    height: 297px;
    overflow: hidden;
  }
  .card-front { left: 60px; background: var(--card-white); }
  .card-back { left: 620px; background: var(--card-dark); }

  .brand {
    font-family: "Cinzel", Georgia, serif;
    font-weight: 600;
    text-align: center;
    line-height: 1.05;
    letter-spacing: 1px;
  }
  .front-brand {
    position: absolute;
    left: 30px;
    top: 100px;
    width: 200px;
    color: var(--ink);
    font-size: 29px;
  }
  .front-brand .brand-sub { font-size: 19px; letter-spacing: 2px; }

  .divider {
    position: absolute;
    left: 252px;
    top: 46px;
    width: 1px;
    height: 200px;
    background: var(--rule-grey);
  }
  .contact {
    position: absolute;
    left: 276px;
    top: 50px;
    width: 230px;
    color: var(--text-grey);
  }
  .person-name {
    font-family: "Cinzel", Georgia, serif;
    font-weight: 700;
    font-size: 17px;
    color: var(--ink);
    letter-spacing: 0.5px;
  }
  .person-role {
    font-family: "Cinzel", Georgia, serif;
    font-size: 12px;
    color: var(--gold);
    letter-spacing: 0.5px;
    margin-bottom: 8px;
  }
  .address { font-size: 11.5px; line-height: 1.45; margin-bottom: 8px; }
  .contact-list { list-style: none; font-size: 11.5px; line-height: 1.55; }
  .contact-list li { display: flex; align-items: center; gap: 7px; }
  .contact-list svg { width: 11px; height: 11px; flex: none; fill: var(--ink); }

  .band-dark {
    position: absolute; left: 0; bottom: 0;
    width: 57%; height: 12px; background: var(--ink);
  }
  .band-gold {
    position: absolute; right: 0; bottom: 0;
    width: 43%; height: 22px; background: var(--gold);
  }

  .back-brand {
    position: absolute;
    left: 0; right: 0;
    top: 106px;
    color: var(--silver);
    font-size: 38px;
  }
  .back-brand .brand-sub { font-size: 24px; letter-spacing: 3px; }
</style>
</head>
<body>

<section class="card card-front" aria-label="Business card front">
  <div class="brand front-brand">Pelham<br><span class="brand-sub">Stoneworks</span></div>
  <div class="divider"></div>
  <div class="contact">
    <p class="person-name">Brian Pelham</p>
    <p class="person-role">Managing Director</p>
    <p class="address">Suite 17, 9 Lambert Lane<br>Kellyville, Sydney NSW 2155</p>
    <ul class="contact-list">
      <li><svg viewBox="0 0 24 24" aria-hidden="true"><path d="M6.6 10.8a15.1 15.1 0 006.6 6.6l2.2-2.2c.3-.3.7-.4 1-.2 1.1.4 2.3.6 3.6.6.6 0 1 .4 1 1V20c0 .6-.4 1-1 1A17 17 0 013 4c0-.6.4-1 1-1h3.5c.6 0 1 .4 1 1 0 1.3.2 2.5.6 3.6.1.3 0 .7-.2 1z"/></svg>02 9563 4820</li>
      <li><svg viewBox="0 0 24 24" aria-hidden="true"><path d="M7 1h10a2 2 0 012 2v18a2 2 0 01-2 2H7a2 2 0 01-2-2V3a2 2 0 012-2zm0 3v14h10V4zm5 15.5a1 1 0 100 2 1 1 0 000-2z"/></svg>0417639285</li>
      <li><svg viewBox="0 0 24 24" aria-hidden="true"><path d="M2 5h20v14H2zm2 2v.5l8 5 8-5V7l-8 5z"/></svg>brian@pelhamstoneworks.com.au</li>
      <li><svg viewBox="0 0 24 24" aria-hidden="true"><path d="M12 2a10 10 0 100 20 10 10 0 000-20zm-1 17.9A8 8 0 014.2 9.6L9 14.4v1a2 2 0 002 2zm6.9-2.5a2 2 0 00-1.9-1.4h-1v-3a1 1 0 00-1-1H8v-2h2a1 1 0 001-1V7h2a2 2 0 002-2v-.4a8 8 0 012.9 12.8z"/></svg>www.pelhamstoneworks.com.au</li>
    </ul>
  </div>
  <div class="band-dark"></div>
  <div class="band-gold"></div>
</section>

<section class="card card-back" aria-label="Business card back">
  <div class="brand back-brand">Pelham<br><span class="brand-sub">Stoneworks</span></div>
</section>

</body>
</html>
```